ALL TEXT GRAPHICS TM May 2025 for Instagram

We are looking for a series of social media graphics for Instagram (new size: 4:5 (1080 x 1350 pixels) ratio that are ALL TEXT. We want the following quotes below on each graphic; one quote per graphic. AND, In very small letters at the bottom of each graphic, add @TovaMarshOnline
The look and feel of these graphics should be complimentary to the color palette attached below; but keep them simple. But the design is up to you; at the end of this document, I provided various samples of all text graphics that I like as examples.
Target Market(s)
women looking to lose weight
Look and feel

```html
<!DOCTYPE html>
<html lang="en">
<head>
<meta charset="utf-8">
<title>All Text Graphics – Tova Marsh</title>
<link rel="stylesheet" href="https://fonts.googleapis.com/css2?family=Poppins:wght@400;500;600;700;800&display=swap">
<style>
  :root {
    --stage: #3d2833;
    --card: #fdcbe7;
    --hot: #f2148d;
    --deep: #e00079;
    --soft: #fa8fc9;
    --blush: #fde3f1;
  }
  * { box-sizing: border-box; margin: 0; padding: 0; }
  html, body { width: 1200px; height: 376px; overflow: hidden; }
  body {
    background: var(--stage);
    font-family: "Poppins", sans-serif;
  }
  .series {
    position: absolute;
    left: 24px;
    top: 113px;
    display: flex;
    gap: 6px;
  }
  .post {
    position: relative;
    width: 109.5px;
    height: 140px;
    background: var(--card);
    padding: 27px 8px 0 15px;
    color: var(--hot);
  }
  .post--tall { padding-top: 21px; }
  .headline {
    font-weight: 800;
    font-size: 10.5px;
    line-height: 0.9;
    text-transform: uppercase;
    letter-spacing: -0.1px;
  }
  .headline--dense {
    font-size: 9.6px;
    line-height: 0.88;
  }
  .headline span { display: block; }
  .body {
    margin-top: 9px;
    font-size: 6px;
    line-height: 1.25;
    font-weight: 400;
  }
  .body--close { margin-top: 6px; }
  .cta {
    margin-top: 9px;
    font-size: 6px;
    font-weight: 700;
    letter-spacing: 1.3px;
    text-transform: uppercase;
    line-height: 1.35;
  }
  .keyword {
    font-weight: 700;
    letter-spacing: 1.1px;
    text-transform: uppercase;
  }
  .handle {
    position: absolute;
    right: 9px;
    bottom: 8px;
    font-size: 3.8px;
    font-style: italic;
    color: var(--hot);
  }
  .c-hot { color: var(--hot); }
  .c-deep { color: var(--deep); }
  .c-soft { color: var(--soft); }
  .c-blush { color: var(--blush); }
  .inline { display: inline !important; }
</style>
</head>
<body>
<main class="series">

  <article class="post">
    <h2 class="headline">
      <span class="c-blush">Tired.</span>
      <span class="c-soft">Moody.</span>
      <span>Stubborn</span>
      <span>Belly Fat.</span>
    </h2>
    <p class="body">Your hormones<br>are screaming<br>for help!</p>
    <p class="cta c-soft">Let’s fix that.</p>
    <p class="handle">@TovaMarshOnline</p>
  </article>

  <article class="post">
    <h2 class="headline">
      <span class="c-soft">That</span>
      <span class="c-soft">Stubborn</span>
      <span class="c-soft">Weight?</span>
      <span>It’s not</span>
      <span>your fault.</span>
    </h2>
    <p class="body">Your hormones<br>are to blame and<br>you’re not alone; but</p>
    <p class="cta c-soft">There is a fix.</p>
    <p class="handle">@TovaMarshOnline</p>
  </article>

  <article class="post">
    <h2 class="headline">
      <span class="c-soft">Your belly</span>
      <span class="c-soft">isn’t fat…</span>
      <span>It’s</span>
      <span>hormonal.</span>
    </h2>
    <p class="body">And here’s how<br>to fix it.</p>
    <p class="body c-soft">Comment <b class="keyword c-hot">Hormones</b><br>if nothing is working.</p>
    <p class="handle">@TovaMarshOnline</p>
  </article>

  <article class="post">
    <h2 class="headline">
      <span class="c-soft">The</span>
      <span class="c-soft">Stubborn</span>
      <span>Belly Fat</span>
      <span>After 40?</span>
    </h2>
    <p class="body">It’s not about calories;<br>it’s about your hormones.</p>
    <p class="cta">Here is the fix!</p>
    <p class="handle">@TovaMarshOnline</p>
  </article>

  <article class="post">
    <h2 class="headline">
      <span class="c-blush">Flat</span>
      <span class="c-blush">Tummy</span>
      <span>in your 40s?</span>
      <span>It’s still</span>
      <span>possible!</span>
    </h2>
    <p class="body">Comment<br><b class="keyword c-soft">Bye Belly</b><br>to get the 10 secrets<br>to a flatter tummy</p>
    <p class="handle">@TovaMarshOnline</p>
  </article>

  <article class="post">
    <h2 class="headline">
      <span class="c-soft">Bloating.</span>
      <span class="c-soft">Muffin top.</span>
      <span>Puffy</span>
      <span>waistline.</span>
    </h2>
    <p class="body">Your body’s<br>screaming for a<br>different kind of fix.</p>
    <p class="cta c-soft">Here it is</p>
    <p class="handle">@TovaMarshOnline</p>
  </article>

  <article class="post">
    <h2 class="headline">
      <span class="c-blush">You’re</span>
      <span class="c-soft">doing all</span>
      <span class="c-soft">the <span class="inline c-blush">“right”</span></span>
      <span class="c-soft">things,</span>
    </h2>
    <p class="body">but your belly<br>won’t go down?</p>
    <p class="cta">Here’s what<br>you haven’t tried.</p>
    <p class="handle">@TovaMarshOnline</p>
  </article>

  <article class="post post--tall">
    <h2 class="headline">
      <span class="c-soft">This</span>
      <span class="c-blush">90-day</span>
      <span class="c-blush">plan <span class="inline c-soft">helped</span></span>
      <span class="c-deep">Women</span>
      <span><span class="inline c-deep">over 40</span> <span class="inline c-soft">slim</span></span>
      <span class="c-soft">down,</span>
    </h2>
    <p class="body">get a tiny waist<br>and feel sexy again.</p>
    <p class="cta">You’re next.</p>
    <p class="handle">@TovaMarshOnline</p>
  </article>

  <article class="post post--tall">
    <h2 class="headline headline--dense">
      <span class="c-blush">This is</span>
      <span class="c-blush">the secret</span>
      <span class="c-deep">women</span>
      <span class="c-deep">over 40 are</span>
      <span class="c-soft">using to get</span>
      <span class="c-soft">snatched;</span>
      <span class="c-soft">without</span>
      <span class="c-blush">starving</span>
    </h2>
    <p class="body body--close">Comment<br><b class="keyword">Skinny</b><br>to get the exact plan.</p>
    <p class="handle">@TovaMarshOnline</p>
  </article>

  <article class="post">
    <h2 class="headline">
      <span class="c-soft">What</span>
      <span class="c-soft">worked in</span>
      <span class="c-deep">your 30s</span>
      <span class="c-deep">won’t</span>
      <span class="c-deep">work now.</span>
    </h2>
    <p class="body c-deep">Here’s what<br>actually does.<br>Drop 30 Pounds</p>
    <p class="cta">In 3 months.</p>
    <p class="handle">@TovaMarshOnline</p>
  </article>

</main>
</body>
</html>
```